Web Site Redesign for Quellorainc.example

- Introduction

This is a web site redesign content. Please follow the following instructions. I am on tight schedule, so instead of 10 days, I would like to select the final design within 7 days. After the final design is selected, I would like the winner to produce the static HTML pages, but that is a separate job.

Delivery is JPG, complete Layered PSD files, and color numbers used in the design.

- Language of Content of the Web Site: English

- Company Name: Quellora, Inc.

- What is Quellora, Inc.'s product? Company develops and markets a sophisticated engineering simulation software.

- URL of existing web site: http://www.quellorainc.example

- Purpose of the web site: Marketing Engineering and Simulation Software

- Markets/Industries served

1. Medical: Radiotheraphy, Cancer Therapy, Medical Imaging
2. Energy: Nuclear Physics
3. National Security: Dept. of Coastal Surveying

- Three most important messages to communicate to our audience:

1. A solid and sophisticated engineering company (sophisticated).
2. A company with cutting-edge technology and leading products (cutting edge)
3. A company with state-of-art, live and professional marketing (state-of-the-art and live)

- What differentiates Quellora, Inc. from other competitors?

1. We are a commercial company vs. a home-grown entity with competitor products.
2. Our software is in-depth and targeted application vs. a general software with certain capabilities.

- Desired homepage screen size: 1280x800 or use your best recommendation.

- Number of templates: 2
1. Homepage
2. Secondary pages

- What content must be included in the Homepage (video, slideshow, etc.)?

1. Header block to display the logo, company name, and login or registration space (if user is logged in, show username)
2. One primary block to display a slide presentation (in HTML5, up to 4 or 5 slides with combined image and text)
3. One block to display a video and ability to play the video with a link "More" to go to the Video Training page.
4. One block to display announcements and special events
5. One block to display up to three News/Events. A Caption and Date.
6. One block to showcase links to three social networks: Chatterfold, Workloom, and Pipsqueal.
7. One block for Footer. Standard links and copyright notice

- Describe secondary pages: They will include text and images (JPG or PNG). A Training page will display a list of (up to 5) video clips.

- Site Menu Structure

1. Top Level. Up to 6 main menu as follows: Products, Support, Partners, Company, News/Events, and Purchase.

2. Second Level. Each top-level menu could have up to 4 sub-menu options. Some like Partners will not have any page. You don't have to display Third-level menus here.

3. Third Level. Some second-level menu items could have from up to 4 sub-menu options. Third-level menu options should appear in the template for secondary pages.

For example, under main menu "Products" we have three products one of which is "Borvek3QXRT." This product will have 4 options (4 pages). The template for the secondary pages should be flexible enough to allow for more than 4 but less than 6-7 options for each product.

(I will upload the Site Map document shortly)

- Style/theme of the Website:
1. Large enough font size. Audience is 30 and older.
2. Appealing to users of a highly-sophisticated desktop-based simulation software

- Desirable colors in the new design: Blue (because of logo), red, green, gray, black. White or Black background

- Adjectives that should best describe the new design: Welcoming, exciting, informative, and professional

- Websites you like (because?):

http://www.mendalux.example. Only because they also develop sophisticated software and they follow a similar licensing scheme, but PLEASE do not copy their UI.

Target Market(s)

- Age: 30 years and older
- Mostly male.
- Job Title: Researchers, Doctors, and Engineers
- Users of radiotheraphy, cancer therapy, medical imaging, nuclear energy, and homeland security radiation simulation software

Industry/Entity Type

Marketing

Requirements
Must have
• - What content must be included in the Homepage (video, slideshow, etc.)?

7. One block for Footer. Standard links and copyright notice.
Nice to have
• As you see I gave a thorough and detail design brief (I hope so). I leave it to you to incorporate "nice to haves" in your design.
Should not have
• - No Cartoonish Design or Animation
- Colors we do you NOT like: Purple, Pink, Yellow, Brown

```html
<!DOCTYPE html>
<html lang="en">
<head>
<meta charset="utf-8">
<title>Quellora, Inc. – Radiation Transport Simulations</title>
<link href="https://fonts.googleapis.com/css2?family=PT+Sans:ital,wght@0,400;0,700;1,400&family=PT+Sans+Narrow:wght@400;700&display=swap" rel="stylesheet">
<style>
:root{
  --blue:#1a3f9c;
  --blue-dark:#0f2f86;
  --blue-light:#2c5bc4;
  --text:#333;
  --muted:#666;
  --gray-box:#5b5b5b;
  --green:#5a9c2a;
  --red:#c0261c;
  --panel-line:#e2e2e2;
  --white:#fff;
}
*{box-sizing:border-box;margin:0;padding:0}
html,body{width:1069px;height:1200px;overflow:hidden;background:var(--white)}
body{font-family:"PT Sans",sans-serif;color:var(--text);position:relative}
.abs{position:absolute}

/* header */
.brand{left:96px;top:18px;display:flex;align-items:center;gap:8px}
.brand-mark{width:26px;height:26px;background:var(--blue)}
.brand-name{font-family:"PT Sans",sans-serif;font-weight:700;font-size:17px;letter-spacing:4px;color:var(--blue-dark);line-height:1}
.brand-tag{font-size:9px;letter-spacing:1.6px;color:var(--blue-dark);font-weight:700;display:block;margin-top:2px}
.cert-badge{left:898px;top:5px;width:49px;height:58px;background:#111;border:2px solid #333}

/* nav */
.main-nav{left:0;top:72px;width:1069px;height:45px;background:linear-gradient(#2d5fc6,#16409d);border-bottom:2px solid var(--white);box-shadow:0 2px 0 #16409d}
.main-nav ul{list-style:none;display:flex;gap:30px;padding-left:116px;height:100%;align-items:center}
.main-nav li{color:var(--white);font-size:15.5px;text-transform:uppercase}

/* hero */
.hero{left:0;top:119px;width:1069px;height:384px;overflow:hidden}
.hero-photo-left{left:0;top:0;width:686px;height:384px;background:linear-gradient(120deg,#1f2a2a 0%,#6b5546 35%,#2f5fd0 70%,#1d3fae 100%)}
.hero-photo-right{left:686px;top:0;width:383px;height:384px;background:radial-gradient(circle at 55% 45%,#d23b3b 0%,#4a5fd0 35%,#102a7a 70%,#061030 100%)}
.hero-caption{left:0;top:310px;width:1069px;height:74px;background:rgba(24,60,150,.82)}
.hero-caption p{position:absolute;left:0;width:1069px;top:23px;text-align:center;font-family:"PT Sans Narrow",sans-serif;font-weight:700;font-size:23px;color:var(--white)}
.hero-arrow{top:20px;width:35px;height:35px}

/* section titles */
.section-title{font-weight:400;font-size:21px;color:var(--blue);text-transform:uppercase;letter-spacing:-.2px}

/* welcome */
.welcome-title{left:113px;top:530px;font-size:19px}
.welcome-text{left:111px;top:566px;font-size:12.6px;line-height:16px;color:#333}
.welcome-text p{margin-bottom:16px}
.video-thumb{left:476px;top:560px;width:189px;height:127px;border-radius:6px;background:linear-gradient(135deg,#e8e8e8,#b8aaa0 50%,#e4e4e4)}
.btn-more{left:111px;top:760px;width:83px;height:33px;background:#eee;border-radius:3px;color:var(--blue);font-size:14px;line-height:33px;text-align:center;box-shadow:0 1px 2px #bbb}

/* latest news */
.news-panel{left:692px;top:518px;width:273px;height:243px;border:1px solid var(--panel-line)}
.news-head{height:42px;background:linear-gradient(#fafafa,#e9e9e9);border-bottom:1px solid #ddd}
.news-head h2{position:absolute;left:13px;top:11px;font-size:19px}
.pager{width:38px;height:16px}
.date-box{width:57px;height:68px;color:var(--white);text-align:center;line-height:1}
.date-box .yr{display:block;font-size:12px;padding-top:6px}
.date-box .day{display:block;font-size:24px;margin-top:2px}
.date-box .mo{display:block;font-size:14px;font-style:italic;margin-top:3px}
.date-gray{background:var(--gray-box)}
.date-green{background:var(--green)}
.news-text{width:165px;font-size:12.5px;font-style:italic;line-height:21.5px;color:#666}

/* divider */
.hatch{left:6px;top:802px;width:1063px;height:13px;background:repeating-linear-gradient(-55deg,#c9c9c9 0 1px,transparent 1px 4px)}

/* lower columns */
.col-divider{top:826px;width:1px;height:220px;background:linear-gradient(transparent,#ddd 40%,transparent)}
.events-title{left:104px;top:828px}
.event-head{font-style:italic;color:var(--red);font-size:16px;line-height:17px;width:185px;text-align:justify;text-align-last:justify}
.event-body{font-size:12.5px;line-height:16px;color:#666;width:187px}
.social-title{left:427px;top:828px}
.social-item{left:428px;display:flex;align-items:center;gap:15px;font-size:18px;color:#666}
.social-tile{width:46px;height:46px;background:var(--blue-light)}
.products-title{left:687px;top:825px}
.products-panel{left:689px;top:862px;width:280px;height:195px;background:var(--gray-box)}
.product-shot{width:96px;height:68px;border:3px solid var(--white)}
.product-text{font-size:12.5px;line-height:16px;color:#eee;width:135px;text-align:justify}

/* footer */
.footer-curve{left:0;top:1062px;width:1069px;height:30px}
.footer-links{left:0;top:1110px;width:1069px;text-align:center;font-size:14px;color:#333}
.footer-links span{margin:0 9px}
.copyright{left:0;top:1145px;width:1069px;text-align:center;font-size:12.5px;color:#555}
.footer-bar{left:0;top:1188px;width:1069px;height:12px;background:var(--blue-dark)}
</style>
</head>
<body>

<header>
  <div class="abs brand">
    <span class="brand-mark"></span>
    <span><span class="brand-name">QUELLORA INC.</span><span class="brand-tag">Radiation Transport Simulations</span></span>
  </div>
  <div class="abs cert-badge" role="img" aria-label="Quality certification badge"></div>
</header>

<nav class="abs main-nav">
  <ul>
    <li>Home</li><li>Products</li><li>Support</li><li>Partners</li><li>Company</li><li>News/Events</li><li>Contact</li>
  </ul>
</nav>

<section class="abs hero">
  <div class="abs hero-photo-left" role="img" aria-label="Photo of a person talking on a mobile phone with radio waves"></div>
  <div class="abs hero-photo-right" role="img" aria-label="Illustration of a head in profile showing radiation absorption"></div>
  <div class="abs hero-caption">
    <svg class="abs hero-arrow" style="left:192px" viewBox="0 0 35 35"><circle cx="17.5" cy="17.5" r="17.5" fill="#fff"/><path d="M20 10 L13 17.5 L20 25Z" fill="#16409d"/></svg>
    <p>SOPHISTICATED - CUTTING EDGE - STATE-OF-THE-ART AND LIVE !</p>
    <svg class="abs hero-arrow" style="left:842px" viewBox="0 0 35 35"><circle cx="17.5" cy="17.5" r="17.5" fill="#fff"/><path d="M15 10 L22 17.5 L15 25Z" fill="#16409d"/></svg>
  </div>
</section>

<section>
  <h1 class="abs section-title welcome-title">Welcome to our website</h1>
  <div class="abs welcome-text">
    <p style="width:340px">At Quellora, Inc., we develop software solutions for accurately and rapidly predicting the macroscopic behavior of radiation. Since 2002, our products have been used worldwide for a diverse range of industries where radiation effects play an integral role in product performance, safety, and reliability.</p>
    <p style="width:555px"><span style="display:block;width:340px">Our team consists of internationally recognized experts in the research, development and application of radiation simulation</span>software. All of our products are developed and maintained under an ISO 9001:2000 certified quality management system, and we have a proven track record in the development and commercialization of customer specific OEM solutions.</p>
  </div>
  <div class="abs video-thumb" role="img" aria-label="Video still of a consultation between a doctor and a patient">
    <svg class="abs" style="left:77px;top:46px" width="35" height="35" viewBox="0 0 35 35"><circle cx="17.5" cy="17.5" r="17" fill="rgba(60,60,60,.55)"/><path d="M14 11 L23 17.5 L14 24Z" fill="#fff"/></svg>
  </div>
  <div class="abs btn-more">READ MORE</div>
</section>

<aside class="abs news-panel">
  <div class="news-head">
    <h2 class="section-title">Latest News</h2>
    <svg class="abs pager" style="left:217px;top:16px" viewBox="0 0 38 16"><circle cx="8" cy="8" r="8" fill="#1a3f9c"/><path d="M10 4 L5 8 L10 12Z" fill="#fff"/><circle cx="30" cy="8" r="8" fill="#1a3f9c"/><path d="M28 4 L33 8 L28 12Z" fill="#fff"/></svg>
  </div>
  <div class="abs date-box date-gray" style="left:15px;top:52px"><span class="yr">2013</span><span class="day">06</span><span class="mo">Sep</span></div>
  <p class="abs news-text" style="left:84px;top:50px">Sed ut perspiciatis unde omnis iste natus error sit voluptatem accusantium doloremque l</p>
  <div class="abs date-box date-gray" style="left:15px;top:144px"><span class="yr">2013</span><span class="day">06</span><span class="mo">Sep</span></div>
  <p class="abs news-text" style="left:84px;top:141px">Sed ut perspiciatis unde omnis iste natus error sit voluptatem accusantium doloremque l</p>
</aside>

<div class="abs hatch"></div>

<section>
  <h2 class="abs section-title events-title">Special Events</h2>
  <svg class="abs pager" style="left:325px;top:831px" viewBox="0 0 38 16"><circle cx="8" cy="8" r="8" fill="#1a3f9c"/><path d="M10 4 L5 8 L10 12Z" fill="#fff"/><circle cx="30" cy="8" r="8" fill="#1a3f9c"/><path d="M28 4 L33 8 L28 12Z" fill="#fff"/></svg>
  <p class="abs event-head" style="left:106px;top:868px">Lorem Ipsum is simply dummy text of the printing</p>
  <p class="abs event-body" style="left:106px;top:906px">Sed ut perspiciatis unde omnis iste natus error sit voluptatem accusantium doloremque</p>
  <div class="abs date-box date-green" style="left:305px;top:870px"><span class="yr">2013</span><span class="day">06</span><span class="mo">Sep</span></div>
  <p class="abs event-head" style="left:106px;top:967px">Lorem Ipsum is simply dummy text of the printing</p>
  <p class="abs event-body" style="left:106px;top:1005px">Sed ut perspiciatis unde omnis iste natus error sit voluptatem accusantium doloremque</p>
  <div class="abs date-box date-green" style="left:305px;top:969px"><span class="yr">2013</span><span class="day">06</span><span class="mo">Sep</span></div>
</section>

<div class="abs col-divider" style="left:380px"></div>

<section>
  <h2 class="abs section-title social-title">Social</h2>
  <div class="abs social-item" style="top:877px"><span class="social-tile" style="background:#1e4aa8"></span>Chatterfold</div>
  <div class="abs social-item" style="top:931px"><span class="social-tile" style="background:#3aa0dc"></span>Pipsqueal</div>
  <div class="abs social-item" style="top:986px"><span class="social-tile" style="background:#16589a"></span>Workloom</div>
</section>

<div class="abs col-divider" style="left:668px"></div>

<section>
  <h2 class="abs section-title products-title">Products</h2>
  <svg class="abs pager" style="left:925px;top:829px" viewBox="0 0 38 16"><circle cx="8" cy="8" r="8" fill="#1a3f9c"/><path d="M10 4 L5 8 L10 12Z" fill="#fff"/><circle cx="30" cy="8" r="8" fill="#1a3f9c"/><path d="M28 4 L33 8 L28 12Z" fill="#fff"/></svg>
  <div class="abs products-panel">
    <div class="abs product-shot" style="left:15px;top:21px;background:linear-gradient(120deg,#0a1a2a,#4aa0c8 50%,#e0d8a0)" role="img" aria-label="Radiation dose simulation render of a head"></div>
    <p class="abs product-text" style="left:131px;top:28px">Sed ut perspiciatis unde omnis iste natus error sit voluptatem accusantium doloremque</p>
    <div class="abs product-shot" style="left:15px;top:106px;background:linear-gradient(90deg,#3a8ac0,#6ad060 45%,#e8d040 70%,#4aa0c8)" role="img" aria-label="Radiation field simulation render around a figure"></div>
    <p class="abs product-text" style="left:131px;top:110px">Sed ut perspiciatis unde omnis iste natus error sit voluptatem accusantium doloremque</p>
  </div>
</section>

<footer>
  <svg class="abs footer-curve" viewBox="0 0 1069 30" preserveAspectRatio="none"><path d="M0 2 Q534 40 1069 2 L1069 6 Q534 34 0 6Z" fill="#e4e4e4"/></svg>
  <div class="abs footer-links">Home<span>|</span>Products<span>|</span>Company<span>|</span>Terms<span>|</span>Privacy<span>|</span>Contact</div>
  <div class="abs copyright">© 2013.www.yourfirm.example</div>
  <div class="abs footer-bar"></div>
</footer>

</body>
</html>
```